Driving School Business card design

Hi, we are starting a new business (Driving School) and would like your help with our business card design.
We are located in Adelaide SA.
Our aim is to help young people achieve best possible results by promoting safe and stress free driving.

Name of our school is "Velmira" which means best or most favorable.

Hope there is someone out there in wonderful world of design who can think outside of square and give us recognizable/ unique business card design.

Target Market(s)

16+

Industry/Entity Type

Business

Contact Information for Business Card

Name of our business is "Velmira driver training"
Our idea is to make letter "L' in Velmira more distinct (noticeable) by different color or font, so it gets associated with learner driver.
We like combination of white, dark gray and yellow but do not limit our self to that.
Reverse side of our card would have to incorporate writing space for date and time of the next lesson.

Requirements
Must have
• Business name: Velmira driver training
• Owner/ instructor name
• Mobile no:
• Chatterloop logo
Should not have
• Anything Not associated with driving

```html
<!DOCTYPE html>
<html lang="en">
<head>
<meta charset="utf-8">
<title>Velmira Driver Training – Business Card</title>
<link rel="stylesheet" href="https://fonts.googleapis.com/css2?family=Source+Sans+3:wght@400;600;700&display=swap">
<style>
  :root {
    --stage: #000000;
    --card-top: #38393c;
    --card-bottom: #2c2d30;
    --accent: #f2ec3a;
    --logo-grey: #6b6c6f;
    --divider: #45464a;
    --ink-light: #ffffff;
    --ink-dark: #111111;
    --band: #ffffff;
  }
  * { margin: 0; padding: 0; box-sizing: border-box; }
  html, body {
    width: 1200px; height: 900px; overflow: hidden;
    background: var(--stage);
    font-family: "Source Sans 3", "Myriad Pro", Arial, sans-serif;
  }
  .canvas { position: relative; width: 1200px; height: 900px; }

  .card {
    position: absolute; top: 271px; height: 282px;
    border-radius: 14px;
    background: linear-gradient(180deg, var(--card-top), var(--card-bottom));
    overflow: hidden;
  }
  .card--front { left: 137px; width: 457px; }
  .card--back  { left: 626px; width: 458px; height: 281px; }

  /* Front */
  .brand {
    position: absolute; left: 50px; top: 94px; width: 180px;
    color: var(--logo-grey); font-weight: 400; text-transform: uppercase;
  }
  .brand__row { display: flex; align-items: center; gap: 8px; height: 60px; }
  .brand__dot {
    width: 46px; height: 46px; border-radius: 50%;
    background: var(--accent); flex: none;
  }
  .brand__word { font-size: 30px; line-height: 1; letter-spacing: 0; white-space: nowrap; }
  .brand__sub  {
    display: block; font-size: 16px; line-height: 1; letter-spacing: 1.5px;
    margin-top: 9px; white-space: nowrap;
  }

  .divider {
    position: absolute; left: 243px; top: 81px;
    width: 1px; height: 110px; background: var(--divider);
  }
  .contact { position: absolute; left: 273px; top: 100px; }
  .contact__name {
    color: var(--accent); font-weight: 600; font-size: 17px; margin-bottom: 19px;
  }
  .contact__line {
    display: flex; align-items: center; gap: 7px;
    color: var(--ink-light); font-size: 12.5px; height: 19px; white-space: nowrap;
  }
  .contact__line svg { width: 9px; height: 9px; flex: none; }

  .social {
    position: absolute; left: 0; right: 0; top: 226px;
    display: flex; justify-content: center; align-items: center; gap: 6px;
    color: var(--ink-light); font-size: 12px; font-weight: 600;
  }
  .social__mark { width: 12px; height: 12px; background: var(--accent); border-radius: 2px; }

  /* Back */
  .appointment__title {
    position: absolute; top: 57px; left: 0; right: 0; text-align: center;
    color: var(--accent); font-weight: 600; font-size: 19px;
  }
  .appointment__band {
    position: absolute; top: 88px; left: 0; right: 0; height: 96px;
    background: var(--band);
  }
  .appointment__field {
    position: absolute; left: 100px;
    color: var(--ink-dark); font-weight: 600; font-size: 12px; letter-spacing: .2px;
  }
  .appointment__field--date { top: 28px; }
  .appointment__field--time { top: 72px; }
  .appointment__note {
    position: absolute; top: 198px; left: 0; right: 0; text-align: center;
    color: var(--accent); font-weight: 600; font-size: 16px; line-height: 20px;
  }
</style>
</head>
<body>
<main class="canvas">

  <section class="card card--front" aria-label="Business card front">
    <div class="brand">
      <div class="brand__row">
        <span class="brand__dot" aria-hidden="true"></span>
        <span class="brand__word">Velmira</span>
      </div>
      <span class="brand__sub">Driver Training</span>
    </div>

    <div class="divider" aria-hidden="true"></div>

    <div class="contact">
      <p class="contact__name">Marcus Hale</p>
      <p class="contact__line">
        <svg viewBox="0 0 10 10" aria-hidden="true"><path d="M2 0.6 L3.6 2.8 L2.7 3.8 Q3.6 5.8 6.2 7.3 L7.2 6.4 L9.4 8 L8.3 9.4 Q4.8 9.4 2.3 6.6 Q0.4 4 0.6 1.6 Z" fill="#f2ec3a"/></svg>
        (044)-318-2265
      </p>
      <p class="contact__line">
        <svg viewBox="0 0 10 10" aria-hidden="true"><circle cx="5" cy="5" r="4.6" fill="#f2ec3a"/><path d="M5 .4 V9.6 M.4 5 H9.6 M5 .4 Q2 5 5 9.6 M5 .4 Q8 5 5 9.6" stroke="#2f3033" stroke-width=".8" fill="none"/></svg>
        www.velmiradriving.com
      </p>
    </div>

    <div class="social">
      <span class="social__mark" aria-hidden="true"></span>
      <span>Chatterloop</span>
    </div>
  </section>

  <section class="card card--back" aria-label="Business card back">
    <h2 class="appointment__title">Your Next Appointment is</h2>
    <div class="appointment__band">
      <p class="appointment__field appointment__field--date">Date: ........................................................</p>
      <p class="appointment__field appointment__field--time">Time: ....................... AM....................... PM</p>
    </div>
    <p class="appointment__note">If unable to keep appointment,<br>kindly give 24hrs notice.</p>
  </section>

</main>
</body>
</html>
```